Home Health Company Needs a Corporate Identity Package

We need a corporate identity package (see what it should include below) for a home health care company. The design should be professional, uncluttered, simple and created in Publisher (so that we can edit the design in the future, if necessary. )
We need the following created:
-Presentation folder
-Business card template (color, double sided)
-Letterhead
-Stationary
-postcard sized marketing piece (5.5" x 8.5", color, double sided)

Target Market(s)

We are in the business of supplying personal care aids for in home care. Our services are directed towards older, retired individuals with some disability or illness. However, we will be marketing to the children or relatives of our in home clients. We want our logo to emphasize our reliability and personalized services.

Industry/Entity Type

Home Health Care

Requirements
Must have
• The design should be professional, uncluttered, simple and created in Publisher (so that we can edit the design in the future, if necessary. )

```html
<!DOCTYPE html>
<html lang="en">
<head>
<meta charset="utf-8">
<title>Evenfield Home Care – Letterhead</title>
<link rel="stylesheet" href="https://fonts.googleapis.com/css2?family=Montserrat:wght@700&family=Questrial&display=swap">
<style>
  :root {
    --backdrop: #ececee;
    --paper: #ffffff;
    --ink: #3a3a3e;
    --ink-soft: #6b6b72;
    --brand-blue: #4aaedb;
    --brand-grey: #65656c;
    --signature-tone: #c9cde6;
  }
  * { box-sizing: border-box; margin: 0; padding: 0; }
  html, body {
    width: 1200px; height: 936px; overflow: hidden;
    background: var(--backdrop);
  }
  body {
    font-family: "Questrial", "Century Gothic", sans-serif;
    color: var(--ink);
  }
  .letterhead {
    position: absolute;
    left: 290px; top: 30px;
    width: 620px; height: 876px;
    background: var(--paper);
    box-shadow: 0 2px 10px rgba(0,0,0,0.08);
  }
  .brand {
    position: absolute;
    top: 48px; right: 58px;
    display: flex; align-items: center; gap: 8px;
  }
  .brand-dot {
    width: 22px; height: 22px; border-radius: 50%;
    background: var(--brand-blue);
  }
  .brand-name {
    font-family: "Montserrat", sans-serif;
    font-weight: 700; font-size: 17px;
    color: var(--brand-blue);
    letter-spacing: 0.2px;
  }
  .letter {
    position: absolute;
    left: 62px; top: 190px; width: 470px;
  }
  .salutation {
    font-family: "Montserrat", sans-serif;
    font-weight: 700; font-size: 11px;
    margin-bottom: 8px;
  }
  .letter p {
    font-size: 8.4px; line-height: 1.5;
    margin-bottom: 14px;
    color: var(--ink);
  }
  .sign-off {
    position: absolute;
    right: 62px; top: 560px;
    text-align: right;
  }
  .sign-off .closing { font-size: 8.6px; color: var(--ink); }
  .sign-off .signer {
    font-family: "Montserrat", sans-serif;
    font-weight: 700; font-size: 11px; margin-top: 2px;
  }
  .signature {
    position: absolute;
    right: 130px; top: 600px;
    width: 130px; height: 46px;
    background: linear-gradient(90deg, var(--signature-tone), #e4e6f3);
    border-radius: 4px;
  }
  .website {
    position: absolute;
    left: 62px; bottom: 26px;
    font-size: 8px; letter-spacing: 4.5px;
    color: var(--ink-soft);
  }
  .website .domain { color: var(--brand-blue); }
  .address {
    position: absolute;
    right: 22px; bottom: 24px;
    text-align: right;
    font-size: 6.6px; line-height: 1.5;
    color: var(--ink-soft);
  }
  .address .label { color: var(--brand-blue); font-weight: 700; }
  .footer-band {
    position: absolute; left: 0; right: 0; bottom: 0;
    height: 10px; display: flex;
  }
  .footer-band .band-blue { flex: 0 0 60%; background: var(--brand-blue); }
  .footer-band .band-grey { flex: 1; background: var(--brand-grey); }
</style>
</head>
<body>
  <main class="letterhead">
    <header class="brand">
      <span class="brand-dot"></span>
      <span class="brand-name">Evenfield Home Care</span>
    </header>

    <section class="letter">
      <h1 class="salutation">Dear sir / madame,</h1>
      <p>Lorem ipsum dolor sit amet, consectetur adipisicing elit, sed do eiusmod tempor incididunt ut labore et dolore magna aliqua. Ut enim ad minim veniam, quis nostrud exercitation ullamco laboris nisi ut aliquip ex ea commodo consequat. Duis aute irure dolor in reprehenderit in voluptate velit esse cillum dolore eu fugiat nulla pariatur. Excepteur sint occaecat cupidatat non proident, sunt in culpa qui officia deserunt mollit anim id est laborum. Lorem ipsum dolor sit amet, consectetur adipisicing elit, sed do eiusmod tempor incididunt ut labore et dolore magna aliqua. Ut enim ad minim veniam, quis nostrud exercitation ullamco laboris nisi ut aliquip ex ea commodo consequat. Duis aute irure dolor in reprehenderit in voluptate velit esse cillum dolore eu fugiat nulla pariatur. Excepteur sint occaecat cupidatat non proident, sunt in culpa qui officia deserunt mollit anim id est laborum.</p>
      <p>Lorem ipsum dolor sit amet, consectetur adipisicing elit, sed do eiusmod tempor incididunt ut labore et dolore magna aliqua. Ut enim ad minim veniam, quis nostrud exercitation ullamco laboris nisi ut aliquip ex ea commodo consequat. Duis aute irure dolor in reprehenderit in voluptate velit esse cillum dolore eu fugiat nulla pariatur. Excepteur sint occaecat cupidatat non proident, sunt in culpa qui officia deserunt mollit anim id est laborum.</p>
      <p>Lorem ipsum dolor sit amet, consectetur adipisicing elit, sed do eiusmod tempor incididunt ut labore et dolore magna aliqua. Ut enim ad minim veniam, quis nostrud exercitation ullamco laboris nisi ut aliquip ex ea commodo consequat. Duis aute irure dolor in reprehenderit in voluptate velit esse cillum dolore eu fugiat nulla pariatur. Excepteur sint occaecat cupidatat non proident, sunt in culpa qui officia deserunt mollit anim id est laborum.</p>
      <p>Lorem ipsum dolor sit amet, consectetur adipisicing elit, sed do eiusmod tempor incididunt ut labore et dolore magna aliqua. Ut enim ad minim veniam, quis nostrud exercitation ullamco laboris nisi ut aliquip ex ea commodo consequat. Duis aute irure dolor in reprehenderit in voluptate velit esse cillum dolore eu fugiat nulla pariatur. Excepteur sint occaecat cupidatat non proident, sunt in culpa qui officia deserunt mollit anim id est laborum.</p>
    </section>

    <div class="sign-off">
      <div class="closing">Yours Sincerely,</div>
      <div class="signer">Lorna Pell</div>
    </div>
    <div class="signature" role="img" aria-label="Handwritten signature of Lorna Pell"></div>

    <div class="website">www.<span class="domain">evenfieldcare</span>.com</div>
    <address class="address">
      P.O. Box 4417, Harbour Post Office, NSW 2011, Australia<br>
      <span class="label">T:</span> +61 2 5550 1842 &nbsp;<span class="label">E:</span> info@evenfieldcare.com
    </address>

    <div class="footer-band"><span class="band-blue"></span><span class="band-grey"></span></div>
  </main>
</body>
</html>
```